Safety Starts at The Top

Want to make a poster showing our company president in full safety gear (see attached photo) encouraging how "Safety Starts at the Top" We encourage creativity. Visit our website for ideas about our company. www.halvorbuilders.com Our main colors are blue and black, but we will allow other colors to make the poster pop and stand out.

Industry/Entity Type

It Company

Colors
0255a3

Requirements
Must have
• -Must have the photo attached somewhere on the poster. Must have a PPE List which can be creative or bullet points 1. Hard Hat 2. Safety Glasses 3. Shirt with Sleeves, 4. Reflective Vest 5. Gloves 6. Long Pants 7. Safety Boots
• -Must have title "Safety Starts at the Top"
• -Must have a box or section that says the following"Because of our company's core value of RESPECT FOR ALL PEOPLE the commitment to Safety Starts at the Top. Halvor Builders’s most valuable asset is our team members, which is why I take personal responsibility for our safety culture. It is our daily mission for every team member to return home to their families without injuries, giving them a life away from work that can be enjoyed."

```html
<!DOCTYPE html>
<html lang="en">
<head>
<meta charset="UTF-8">
<title>Halvor Builders – Safety Starts at the Top</title>
<link rel="stylesheet" href="https://fonts.googleapis.com/css2?family=Bebas+Neue&family=Oswald:wght@500;700&family=Roboto+Condensed:wght@400;700&display=swap">
<style>
  :root {
    --paper: #ffffff;
    --navy: #0f1f5e;
    --ink: #121212;
    --brand-blue: #0255a3;
    --city-cool: #8fa3ad;
    --city-mid: #f0c77a;
    --city-warm: #ee6a4e;
    --vest: #d7e84a;
    --helmet: #1f47b8;
    --trousers: #a39c8c;
    --panel: rgba(255, 255, 255, 0.92);
  }
  html, body {
    margin: 0;
    padding: 0;
    width: 1200px;
    height: 927px;
    overflow: hidden;
    background: var(--paper);
  }
  .poster {
    position: relative;
    width: 1200px;
    height: 927px;
    background: var(--paper);
    overflow: hidden;
  }
  .city-skyline {
    position: absolute;
    left: 0;
    bottom: 0;
    width: 1200px;
    height: 440px;
    background: linear-gradient(90deg, var(--city-cool) 0%, #c9cfc8 35%, var(--city-mid) 60%, var(--city-warm) 100%);
    -webkit-mask-image: linear-gradient(180deg, transparent 0%, #000 30%);
            mask-image: linear-gradient(180deg, transparent 0%, #000 30%);
    opacity: 0.85;
  }
  .president-photo {
    position: absolute;
    left: 30px;
    top: 40px;
    width: 360px;
    height: 887px;
    border-radius: 140px 140px 10px 10px;
    background: linear-gradient(180deg, var(--helmet) 0%, #d9b89a 12%, var(--vest) 22%, var(--vest) 52%, var(--trousers) 62%, var(--trousers) 93%, #2a2a2a 100%);
  }
  .content {
    position: absolute;
    left: 440px;
    width: 680px;
  }
  .brand-lockup {
    top: 52px;
    display: flex;
    justify-content: center;
    align-items: center;
    gap: 16px;
  }
  .brand-mark {
    width: 84px;
    height: 84px;
    background: var(--navy);
  }
  .brand-name {
    font-family: 'Oswald', sans-serif;
    font-weight: 700;
    color: var(--navy);
    line-height: 0.95;
    text-transform: uppercase;
  }
  .brand-name .primary { display: block; font-size: 62px; letter-spacing: 1px; }
  .brand-name .secondary { display: block; font-size: 27px; letter-spacing: 3px; text-align: center; }
  .headline {
    top: 178px;
    margin: 0;
    text-align: center;
    font-family: 'Bebas Neue', sans-serif;
    font-weight: 400;
    color: var(--navy);
    line-height: 0.9;
  }
  .headline .line-one { display: block; font-size: 112px; }
  .headline .line-two { display: block; font-size: 152px; }
  .commitment {
    top: 448px;
    box-sizing: border-box;
    margin: 0;
    padding: 12px 18px;
    background: var(--panel);
    border-left: 6px solid var(--brand-blue);
    font-family: 'Roboto Condensed', sans-serif;
    font-size: 15px;
    line-height: 1.38;
    color: var(--ink);
  }
  .commitment strong { color: var(--brand-blue); font-weight: 700; }
  .ppe {
    top: 612px;
    margin: 0;
  }
  .ppe-title {
    margin: 0 0 6px;
    text-align: center;
    font-family: 'Oswald', sans-serif;
    font-weight: 700;
    font-size: 18px;
    letter-spacing: 2px;
    color: var(--navy);
    text-transform: uppercase;
  }
  .ppe-list {
    list-style: none;
    margin: 0;
    padding: 0;
    display: flex;
    flex-wrap: wrap;
    justify-content: center;
    gap: 6px 8px;
  }
  .ppe-item {
    padding: 3px 10px;
    background: var(--navy);
    color: var(--paper);
    font-family: 'Oswald', sans-serif;
    font-weight: 500;
    font-size: 16px;
    line-height: 1.3;
  }
  .website {
    top: 738px;
    margin: 0;
    text-align: center;
    font-family: 'Oswald', sans-serif;
    font-weight: 700;
    font-size: 46px;
    line-height: 1.1;
    color: var(--ink);
  }
  .social {
    top: 810px;
    display: flex;
    justify-content: center;
    align-items: center;
    gap: 14px;
  }
  .social-label {
    font-family: 'Oswald', sans-serif;
    font-weight: 500;
    font-size: 24px;
    color: var(--navy);
    text-transform: uppercase;
    margin-right: 6px;
  }
  .social-square {
    width: 38px;
    height: 38px;
    background: var(--brand-blue);
  }
</style>
</head>
<body>
  <main class="poster">
    <div class="city-skyline" role="img" aria-label="Illustrated city skyline fading from cool blue-grey to warm orange and red"></div>
    <div class="president-photo" role="img" aria-label="Photo of the company president standing in full safety gear: blue hard hat, safety glasses, reflective vest, gloves, long pants and boots"></div>

    <div class="content brand-lockup">
      <div class="brand-mark"></div>
      <div class="brand-name">
        <span class="primary">Halvor</span>
        <span class="secondary">Builders</span>
      </div>
    </div>

    <h1 class="content headline">
      <span class="line-one">Safety Starts</span>
      <span class="line-two">At the Top</span>
    </h1>

    <p class="content commitment">Because of our company's core value of <strong>RESPECT FOR ALL PEOPLE</strong> the commitment to Safety Starts at the Top. Halvor Builders’s most valuable asset is our team members, which is why I take personal responsibility for our safety culture. It is our daily mission for every team member to return home to their families without injuries, giving them a life away from work that can be enjoyed.</p>

    <section class="content ppe">
      <h2 class="ppe-title">PPE Checklist</h2>
      <ol class="ppe-list">
        <li class="ppe-item">1. Hard Hat</li>
        <li class="ppe-item">2. Safety Glasses</li>
        <li class="ppe-item">3. Shirt with Sleeves</li>
        <li class="ppe-item">4. Reflective Vest</li>
        <li class="ppe-item">5. Gloves</li>
        <li class="ppe-item">6. Long Pants</li>
        <li class="ppe-item">7. Safety Boots</li>
      </ol>
    </section>

    <p class="content website">www.halvorbuilders.com</p>

    <div class="content social">
      <span class="social-label">Connect with us</span>
      <span class="social-square"></span>
      <span class="social-square"></span>
      <span class="social-square"></span>
    </div>
  </main>
</body>
</html>
```